Business Card Design for Law firm - already have logo

Now that we have a logo, we need a business card design - our logo is attached -it is salaryman font if that helps - we would like a file that can be uploaded to cardquill (www.cardquill-example.com) using the logo and with the following information on it:
Quenby Law Firm, P.C.
Delwyn Quenby, Esq.
5817 SW 19th Ave.
Alderbrook, ST 00142
555.301.0142 phone
555.301.0187 fax
del@quenby-example.net
voicelink: delquenby
chatline: delwyn.quenby@mailbox-example.com
Target Market(s)
our business cards are distributed to corporate executives, technology professionals and healthcare providers
Industry/Entity Type
Business
Look and feel

```html
<!DOCTYPE html>
<html lang="en">
<head>
<meta charset="utf-8">
<title>Quenby Law Firm, P.C. — Business Card</title>
<link rel="stylesheet" href="https://fonts.googleapis.com/css2?family=Ubuntu:wght@400;500;700&display=swap">
<style>
  :root {
    --backdrop: #3b3b3b;
    --card-white: #ffffff;
    --card-black: #0c0c0c;
    --card-black-glow: #3a3a3a;
    --ink: #141414;
    --rule: #555555;
    --paper-text: #f2f2f2;
  }
  * { box-sizing: border-box; margin: 0; padding: 0; }
  html, body {
    width: 1200px; height: 926px; overflow: hidden;
    background: var(--backdrop);
    font-family: "Ubuntu", "Helvetica Neue", Arial, sans-serif;
  }
  .stage {
    width: 1200px; height: 926px;
    display: flex; flex-direction: column; align-items: center; justify-content: center;
    gap: 56px;
  }
  .card {
    width: 640px; height: 366px; position: relative;
    box-shadow: 0 10px 30px rgba(0,0,0,.45);
  }

  /* Back side */
  .card--back {
    background: radial-gradient(ellipse at 50% 45%, var(--card-black-glow) 0%, var(--card-black) 62%);
    display: flex; align-items: center; justify-content: center;
  }
  .back-lockup { display: flex; flex-direction: column; align-items: flex-end; }
  .back-lockup .wordmark {
    color: var(--paper-text); font-size: 52px; font-weight: 400;
    letter-spacing: 14px; line-height: 1;
  }
  .back-lockup .firm-name {
    color: var(--paper-text); font-size: 13px; font-weight: 500; letter-spacing: 2px;
    text-transform: uppercase; margin-top: 10px; margin-right: 14px;
  }

  /* Front side */
  .card--front { background: var(--card-white); color: var(--ink); }
  .front-lockup { position: absolute; left: 34px; top: 30px; display: flex; flex-direction: column; align-items: flex-end; }
  .front-lockup .wordmark { font-size: 34px; letter-spacing: 9px; line-height: 1; }
  .front-lockup .firm-name { font-size: 9.5px; font-weight: 500; letter-spacing: 1.5px; text-transform: uppercase; margin-top: 6px; margin-right: 8px; }

  .name-row {
    position: absolute; left: 0; right: 26px; top: 130px;
    display: flex; align-items: center;
  }
  .name-row .rule { height: 1.5px; background: var(--rule); }
  .name-row .rule--lead { flex: 1; }
  .name-row .rule--tail { width: 36px; }
  .holder { padding: 0 10px; position: relative; }
  .holder .person { font-size: 24px; font-weight: 700; white-space: nowrap; }
  .holder .title { position: absolute; right: 10px; top: 30px; font-size: 12px; font-weight: 500; }

  .contact {
    position: absolute; left: 30px; top: 196px;
    display: grid; grid-template-columns: 76px auto; row-gap: 3px; column-gap: 8px;
    font-size: 13px;
  }
  .contact dt {
    background: var(--ink); color: var(--card-white);
    font-size: 10.5px; padding: 1px 6px; line-height: 15px;
  }
  .contact dd { line-height: 17px; white-space: nowrap; }
</style>
</head>
<body>
  <main class="stage">
    <section class="card card--back" aria-label="Card back">
      <div class="back-lockup">
        <span class="wordmark">QUENBY</span>
        <span class="firm-name">Quenby Law Firm, P.C.</span>
      </div>
    </section>

    <section class="card card--front" aria-label="Card front">
      <div class="front-lockup">
        <span class="wordmark">QUENBY</span>
        <span class="firm-name">Quenby Law Firm, P.C.</span>
      </div>

      <div class="name-row">
        <span class="rule rule--lead"></span>
        <div class="holder">
          <span class="person">Delwyn Quenby</span>
          <span class="title">Esq</span>
        </div>
        <span class="rule rule--tail"></span>
      </div>

      <dl class="contact">
        <dt>address:</dt><dd>5817 SW 19th Ave. Alderbrook, ST 00142</dd>
        <dt>phone:</dt><dd>555.301.0142</dd>
        <dt>fax:</dt><dd>555.301.0187</dd>
        <dt>email:</dt><dd>del@quenby-example.net</dd>
        <dt>voicelink:</dt><dd>delquenby</dd>
        <dt>chatline:</dt><dd>delwyn.quenby@mailbox-example.com</dd>
      </dl>
    </section>
  </main>
</body>
</html>
```